High-End audio shop owner needs a business card

I need a personal Business Card for my Audio shop which exists since 1962. We offer high Quality brands, professional Attention and run our own repair-service-department. I look for a design which will be printed on high Quality paper and shall convey trust to the Client that we are very serious. Language is german.

```html
<!DOCTYPE html>
<html lang="de">
<head>
<meta charset="utf-8">
<title>Hi-Fi Lindenthal – Visitenkarte</title>
<link rel="stylesheet" href="https://fonts.googleapis.com/css2?family=Montserrat:wght@400;600;800&family=Lato:wght@400;700&display=swap">
<style>
  :root {
    --bg: #24252a;
    --white: #ffffff;
    --orange: #f07124;
    --slate: #7c807b;
    --paper: #e6e6e6;
    --ink: #1c1c1c;
    --rule: #555555;
  }
  * { box-sizing: border-box; margin: 0; padding: 0; }
  html, body { width: 1200px; height: 800px; overflow: hidden; background: var(--bg); }
  .canvas {
    width: 1200px; height: 800px;
    display: flex; align-items: center; justify-content: center; gap: 40px;
  }
  .card {
    width: 540px; height: 310px;
    border-radius: 16px; overflow: hidden;
    position: relative;
  }

  /* Front */
  .card--front { background: var(--white); display: flex; flex-direction: column; }
  .front__brand {
    height: 122px;
    display: flex; align-items: flex-end; justify-content: center;
    padding-bottom: 18px;
  }
  .brand-name {
    font-family: "Montserrat", sans-serif;
    font-weight: 800;
    font-size: 40px;
    letter-spacing: 1px;
    color: var(--orange);
    text-transform: uppercase;
  }
  .front__contact {
    height: 140px;
    background: var(--orange);
    color: var(--white);
    display: flex; flex-direction: column; align-items: center; justify-content: center;
    text-align: center;
  }
  .person-name {
    font-family: "Montserrat", sans-serif;
    font-weight: 800; font-size: 17px; letter-spacing: 1px;
    text-transform: uppercase;
  }
  .person-role {
    font-family: "Lato", sans-serif;
    font-size: 12px; margin-top: 1px; margin-bottom: 12px;
  }
  .contact-line {
    font-family: "Lato", sans-serif;
    font-size: 12.5px;
    display: flex; align-items: center; gap: 6px;
  }
  .contact-line svg { width: 12px; height: 12px; fill: var(--white); }
  .contact-line .divider { margin: 0 4px; }
  .contact-web {
    font-family: "Lato", sans-serif;
    font-size: 12.5px; letter-spacing: 2.5px; margin-top: 5px;
  }
  .front__rule { height: 4px; background: var(--white); }
  .front__address {
    flex: 1;
    background: var(--slate);
    color: var(--white);
    font-family: "Lato", sans-serif;
    font-size: 12.5px; letter-spacing: 1px;
    display: flex; align-items: center; justify-content: center;
  }

  /* Back */
  .card--back { background: var(--paper); padding: 40px 48px 0; }
  .note__title {
    font-family: "Lato", sans-serif;
    font-size: 14px; letter-spacing: 3px;
    color: var(--ink); text-align: center;
    margin-bottom: 14px;
  }
  .note__line { border-bottom: 1.5px dotted var(--rule); height: 26px; }
  .back__brand {
    position: absolute; right: 40px; bottom: 28px;
  }
  .back__brand .brand-name { color: var(--ink); font-size: 28px; }
</style>
</head>
<body>
<main class="canvas">

  <section class="card card--front">
    <div class="front__brand"><span class="brand-name">Hi-Fi Lindenthal</span></div>
    <div class="front__contact">
      <p class="person-name">Paul Weber</p>
      <p class="person-role">Director</p>
      <p class="contact-line">
        <svg viewBox="0 0 24 24" aria-hidden="true"><path d="M6.6 10.8a15.5 15.5 0 0 0 6.6 6.6l2.2-2.2c.3-.3.7-.4 1-.2 1.1.4 2.3.6 3.6.6.6 0 1 .4 1 1V20c0 .6-.4 1-1 1A17 17 0 0 1 3 4c0-.6.4-1 1-1h3.5c.6 0 1 .4 1 1 0 1.3.2 2.5.6 3.6.1.3 0 .7-.2 1z"/></svg>
        <span>(0761) 812 4470</span>
        <span class="divider">|</span>
        <svg viewBox="0 0 24 24" aria-hidden="true"><path d="M2 5h20v14H2z M2 5l10 8 10-8" /></svg>
        <span>info@lindenthal-audio.de</span>
      </p>
      <p class="contact-web">www.lindenthal-audio.de</p>
    </div>
    <div class="front__rule"></div>
    <div class="front__address">Postfach 1962, Gartenstraße 14, Freiburg</div>
  </section>

  <section class="card card--back">
    <h2 class="note__title">NOTE</h2>
    <div class="note__line"></div>
    <div class="note__line"></div>
    <div class="note__line"></div>
    <div class="note__line"></div>
    <div class="note__line"></div>
    <div class="back__brand"><span class="brand-name">Hi-Fi Lindenthal</span></div>
  </section>

</main>
</body>
</html>
```